pathology learning flashcard template graphic design .

Creative designs for 2 sides of the flashcards to include colorful sectioning and font sizes that will make it easy to use in studying.

```html
<!DOCTYPE html>
<html lang="en">
<head>
<meta charset="utf-8">
<title>Gastrointestinal Pathology Case 0001</title>
<link rel="stylesheet" href="https://fonts.googleapis.com/css2?family=Arvo&family=Roboto:ital,wght@0,400;0,500;1,500&display=swap">
<style>
:root{
  --red:#dc2d2b;
  --navy:#1a2066;
  --navy-light:#5a78b4;
  --teal:#2ebfcc;
  --ink:#0f1a44;
  --white:#ffffff;
  --slate:#636e8f;
}
*{margin:0;padding:0;box-sizing:border-box}
html,body{width:1200px;height:824px;overflow:hidden}
body{font-family:"Roboto",sans-serif;background:var(--white)}
.card{position:relative;width:1200px;height:824px;overflow:hidden;
  background:linear-gradient(90deg,var(--navy) 0%,#1c2470 35%,#3a4f98 65%,var(--navy-light) 100%)}
.card-backdrop{position:absolute;left:340px;top:130px;width:860px;height:694px;
  background:radial-gradient(ellipse at 28% 45%,rgba(150,80,140,.35) 0%,rgba(120,90,160,.18) 30%,rgba(0,0,0,0) 60%),
             radial-gradient(ellipse at 70% 30%,rgba(170,180,220,.22) 0%,rgba(0,0,0,0) 55%)}
.subject-band{position:absolute;left:0;top:0;width:1200px;height:122px;background:var(--red);
  border-bottom:8px solid var(--white);display:flex;align-items:center;justify-content:center}
.subject-title{font-family:"Arvo",serif;color:var(--white);font-size:56px;letter-spacing:3px;font-weight:400;margin-top:6px}
.case-tag{position:absolute;left:57px;top:182px;width:641px;height:56px;background:var(--teal);
  display:flex;align-items:center;padding-left:36px}
.case-tag span{font-family:"Arvo",serif;color:var(--ink);font-size:29px;letter-spacing:5px}
.case-image{position:absolute;left:60px;top:282px;width:250px;height:250px;background:var(--slate)}
.case-text{position:absolute;left:354px;top:277px;width:796px;color:var(--white);
  font-size:23px;line-height:38.4px;text-align:justify}
.case-text em{font-weight:500}
.answers{position:absolute;left:358px;top:648px;display:grid;grid-template-columns:268px 320px;
  row-gap:15px;color:var(--white);font-size:23px;font-weight:500}
</style>
</head>
<body>
<main class="card">
  <div class="card-backdrop" role="img" aria-label="Soft medical photograph of an examination scene in blue and violet tones"></div>
  <header class="subject-band"><h1 class="subject-title">GASTROINTESTINAL</h1></header>
  <div class="case-tag"><span>PATHOLOGY CASE ID 0001</span></div>
  <div class="case-image" role="img" aria-label="Case image placeholder"></div>
  <p class="case-text">50-year-old woman comes to the clinic because she has difficulty swallowing for the past few months. She says symptoms have been worsening. She also complains of cough, mostly at night and in fear of choking, has stopped eating many foods, losing about 12 lbs in the past 3 months. Past medical history is unremarkable. Vital signs are normal and physical exam is unremarkable. Chest x-ray with demonstrates an air-fluid level, while manometry shows absent relaxation of the lower esophageal sphincter during swallowing. <em>What is the most likely diagnosis?</em></p>
  <ol class="answers" style="list-style:none">
    <li>A) GERD</li>
    <li>B) Barret Esophagus</li>
    <li>C) Achalasia</li>
    <li>D) Eosinophilic esophagitis</li>
  </ol>
</main>
</body>
</html>
```